Glow-Mist
Your Source for Stealth Vaping Solutions
I need double sided standard sized Business Card [3.5" x 2"]
I'll leave this up to you, play around w/ some different fonts.Keep it professional. I'm a retailer
Professional
Norris Pellgrave
CEO
Do not list an address on the card.
glowmist.staff@kelvora-mail.net
www.cirro-Q.net
A word about my business: We are a web-based retailer which specializes in electronic cigarettes. I'd like the card to look very professional and clean.
Black should be the dominant color in the scheme, or at least the background. If you can add a subtle pattern into the background that would be nice.
identical background, With a fullsized Cirro-Q logo displayed
Cirro-Q logo
the symbol by itself
this is the variation I want used.

```html
<!DOCTYPE html>
<html lang="en">
<head>
<meta charset="utf-8">
<title>Cirro-Q Business Card</title>
<link href="https://fonts.googleapis.com/css2?family=Arimo:wght@400;700&display=swap" rel="stylesheet">
<style>
  :root {
    --backdrop: #dcc39c;
    --card-black: #050505;
    --card-black-soft: #1c1c1c;
    --divider: #d9cfa6;
    --green-center: #b9e23c;
    --green-mid: #5cc843;
    --green-edge: #2aa947;
    --ink: #0b1a0b;
    --brand: #8fcf3a;
    --accent-circle: #f0a020;
  }
  html, body {
    margin: 0;
    padding: 0;
    width: 1200px;
    height: 965px;
    overflow: hidden;
    background: var(--backdrop);
    font-family: "Arimo", Arial, sans-serif;
  }
  .business-card {
    position: absolute;
    left: 243px;
    top: 235px;
    width: 774px;
    height: 450px;
    border-radius: 22px;
    overflow: hidden;
    display: flex;
    box-shadow: 0 6px 16px rgba(0,0,0,0.35);
  }
  .card-front {
    width: 408px;
    height: 100%;
    background: linear-gradient(160deg, var(--card-black-soft) 0%, var(--card-black) 55%);
    position: relative;
    border-right: 3px solid var(--divider);
  }
  .brand-mark {
    position: absolute;
    left: 50%;
    top: 82px;
    width: 72px;
    height: 72px;
    margin-left: -36px;
    border-radius: 50%;
    background: var(--accent-circle);
  }
  .brand-name {
    position: absolute;
    left: 0;
    right: 0;
    top: 222px;
    text-align: center;
    font-size: 56px;
    font-weight: 400;
    letter-spacing: 6px;
    color: var(--brand);
    margin: 0;
  }
  .card-back {
    flex: 1;
    height: 100%;
    position: relative;
    background: radial-gradient(circle at 50% 52%, var(--green-center) 0%, var(--green-mid) 38%, var(--green-edge) 80%);
    color: var(--ink);
  }
  .person {
    position: absolute;
    right: 36px;
    top: 30px;
    text-align: right;
  }
  .person-name {
    margin: 0;
    font-size: 23px;
    font-weight: 700;
  }
  .person-title {
    margin: 3px 0 0;
    font-size: 16px;
  }
  .contact-list {
    position: absolute;
    right: 30px;
    bottom: 26px;
    margin: 0;
    padding: 0;
    list-style: none;
  }
  .contact-item {
    display: flex;
    justify-content: flex-end;
    align-items: center;
    font-size: 17px;
    height: 39px;
  }
  .contact-icon {
    width: 18px;
    height: 18px;
    margin-left: 16px;
  }
</style>
</head>
<body>
  <div class="business-card">
    <section class="card-front">
      <div class="brand-mark"></div>
      <p class="brand-name">CIRRO-Q</p>
    </section>
    <section class="card-back">
      <div class="person">
        <p class="person-name">Norris Pellgrave</p>
        <p class="person-title">CEO</p>
      </div>
      <ul class="contact-list">
        <li class="contact-item">(555) 014-2387
          <svg class="contact-icon" viewBox="0 0 24 24"><path d="M6.6 10.8c1.4 2.8 3.8 5.1 6.6 6.6l2.2-2.2c.3-.3.7-.4 1-.2 1.1.4 2.3.6 3.6.6.6 0 1 .4 1 1V20c0 .6-.4 1-1 1C10.6 21 3 13.4 3 4c0-.6.4-1 1-1h3.5c.6 0 1 .4 1 1 0 1.3.2 2.5.6 3.6.1.3 0 .7-.2 1L6.6 10.8z" fill="var(--ink)"/></svg>
        </li>
        <li class="contact-item">glowmist.staff@kelvora-mail.net
          <svg class="contact-icon" viewBox="0 0 24 24"><circle cx="12" cy="12" r="4" fill="none" stroke="var(--ink)" stroke-width="2.4"/><path d="M16 8v5.5c0 1.7 1.2 2.5 2.5 2.5S21 15 21 12a9 9 0 1 0-3.5 7.1" fill="none" stroke="var(--ink)" stroke-width="2.4"/></svg>
        </li>
        <li class="contact-item">www.cirro-Q.net
          <svg class="contact-icon" viewBox="0 0 24 24"><g fill="none" stroke="var(--ink)" stroke-width="1.8"><circle cx="12" cy="12" r="9"/><ellipse cx="12" cy="12" rx="4" ry="9"/><path d="M3 12h18M5 7h14M5 17h14"/></g></svg>
        </li>
      </ul>
    </section>
  </div>
</body>
</html>
```